Post Lockdown Ortho Special

We are running a special for (Ortho) Braces/Clear Aligner (Quorventa), till July 31st 2020. Up to $2,000 off with free Consultation and Xrays.

We need a ad to run in different formats.

Maybe something with: what better time to get braces when you have to wear a mask all the time.

Trying to rebuild our business and get people in for free consultations.

```html
<!DOCTYPE html>
<html lang="en">
<head>
<meta charset="utf-8">
<title>Ridgeline Family Dentistry – Ortho Special</title>
<link href="https://fonts.googleapis.com/css2?family=Cinzel:wght@400;700&family=Montserrat:wght@700&display=swap" rel="stylesheet">
<style>
  :root {
    --purple: #5b3a8e;
    --purple-mid: #8d6cba;
    --lilac: #c9b5dc;
    --glow: #f3e6dc;
    --ink: #161616;
    --grey-text: #7a7a7a;
    --rule: #b9b9b9;
    --page: #ffffff;
    --stage: #ffffff;
  }
  * { margin: 0; padding: 0; box-sizing: border-box; }
  html, body {
    width: 1200px; height: 1176px; overflow: hidden;
    background: var(--stage);
  }
  .ad {
    position: absolute; left: 50px; top: 164px;
    width: 1015px; height: 782px;
    background: var(--page);
    box-shadow: 0 4px 14px rgba(0,0,0,.28);
    transform: scale(1.0837); transform-origin: top left;
    overflow: hidden;
  }
  .brand { position: absolute; left: 45px; top: 25px; }
  .brand__mark {
    position: absolute; left: 0; top: 20px;
    width: 140px; height: 140px; border-radius: 50%;
    background: var(--purple-mid);
  }
  .brand__name {
    position: absolute; left: 178px; top: 60px; white-space: nowrap;
    font-family: "Cinzel", serif; font-weight: 700; color: var(--purple);
  }
  .brand__title { font-size: 46px; line-height: 48px; letter-spacing: 1px; }
  .brand__sub { font-size: 15px; letter-spacing: 7.5px; line-height: 20px; }
  .brand__doctor {
    position: absolute; left: 178px; top: 136px; width: 292px;
    border-top: 1px solid var(--rule); padding-top: 6px;
    font-family: "Cinzel", serif; font-size: 15px; letter-spacing: 1.2px;
    color: var(--grey-text); text-align: center; white-space: nowrap;
  }
  .offer { position: absolute; left: 55px; top: 225px; font-family: "Cinzel", serif; }
  .offer__date { font-size: 31px; color: var(--ink); line-height: 40px; }
  .offer__upto { font-size: 52px; color: var(--purple); line-height: 60px; margin-top: 6px; }
  .offer__amount { color: var(--purple); line-height: 90px; margin-top: 6px; white-space: nowrap; }
  .offer__amount strong { font-weight: 400; font-size: 86px; }
  .offer__amount span { font-size: 50px; margin-left: 8px; }
  .offer__rule {
    width: 412px; height: 3px; margin-top: 18px;
    background: linear-gradient(90deg, var(--purple), var(--purple) 70%, var(--lilac));
  }
  .offer__extra {
    margin-top: 14px; font-family: "Montserrat", sans-serif; font-weight: 700;
    font-size: 27px; line-height: 33px; color: var(--ink);
  }
  .offer__extra em { font-style: normal; color: var(--purple); }
  .mountains { position: absolute; left: 0; bottom: 0; width: 1015px; height: 210px; }
  .portrait { position: absolute; left: 515px; top: 57px; width: 425px; height: 660px; }
</style>
</head>
<body>
  <main class="ad">
    <header class="brand">
      <div class="brand__mark"></div>
      <div class="brand__name">
        <div class="brand__title">Ridgeline</div>
        <div class="brand__sub">Family Dentistry</div>
      </div>
      <div class="brand__doctor">Dr Helena Marsh</div>
    </header>

    <section class="offer">
      <p class="offer__date">till July 31st 2020</p>
      <p class="offer__upto">Up to</p>
      <p class="offer__amount"><strong>$2,000</strong><span>off</span></p>
      <div class="offer__rule"></div>
      <p class="offer__extra">WITH FREE <em>CONSULTATION</em><br>AND <em>XRAYS</em></p>
    </section>

    <svg class="mountains" viewBox="0 0 1015 210" role="img" aria-label="Illustration of snow-capped purple mountain range">
      <defs>
        <radialGradient id="peakGlow" cx="0.5" cy="0.45" r="0.6">
          <stop offset="0" stop-color="var(--glow)"/>
          <stop offset="0.5" stop-color="var(--lilac)"/>
          <stop offset="1" stop-color="var(--purple-mid)"/>
        </radialGradient>
      </defs>
      <rect x="0" y="0" width="1015" height="210" fill="url(#peakGlow)"/>
    </svg>

    <svg class="portrait" viewBox="0 0 425 660" role="img" aria-label="Photo of a smiling young woman with long brown hair pointing upward">
      <defs>
        <linearGradient id="portraitTone" x1="0" y1="0" x2="0" y2="1">
          <stop offset="0" stop-color="#8a6448"/>
          <stop offset="0.45" stop-color="#b8a99a"/>
          <stop offset="1" stop-color="#a59b90"/>
        </linearGradient>
      </defs>
      <rect x="0" y="0" width="425" height="660" fill="url(#portraitTone)"/>
    </svg>
  </main>
</body>
</html>
```